KV Group

We need a new website for our company and since we had a very good work done for our logo in this site, we're back for the entire job.

Our company name is Marlowe Capital Group. We're adding files of examples of what we have done today. In my opinion we need a more attention lock in the site but yet financial simple work.

Our files (attached) will let you know what we have so far. We need a complete change but the colours should be the same, however you can change them not running away to far from the original, and of course matching with the logo.

We need examples for 3 kind of layouts.

- A HOME welcome layout
- An internal Layout with sidebar
- And internal Layout wide

We can buy image licenses if needed for assets.
Actually there are 5 slide images placed on the Welcome HOME, we need those there, but you can improve with better images to match the new website!!!

Target Market(s)

Clients looking for financial advisers, tax and funds specialist, currency advisers

Industry/Entity Type

Financial

Requirements
Must have
• all the fonts must be in accordance with the financial market sites........the welcome home page must be precise, neat and information accurate........the menu should be elegant........main focus on the Home page, should be also the PRIVATE ACCESS box log in.......

```html
<!DOCTYPE html>
<html lang="en">
<head>
<meta charset="utf-8">
<title>Marlowe Capital Group</title>
<link href="https://fonts.googleapis.com/css2?family=Jost:wght@400;500;600&family=Open+Sans:wght@400;600;700&display=swap" rel="stylesheet">
<style>
:root{
  --brown:#3b1f0a;
  --brown-panel:rgba(74,40,14,.92);
  --orange:#f47b20;
  --ink:#222;
  --text:#333;
  --footer:#222222;
  --footer-line:#3a3a3a;
  --band:#e4e4e4;
  --green:#2e8b1f;
  --red:#d3201c;
  --white:#fff;
}
*{margin:0;padding:0;box-sizing:border-box}
html,body{width:892px;height:1200px;overflow:hidden;background:var(--white)}
body{position:relative;font-family:"Open Sans",Arial,sans-serif;color:var(--text)}
.abs{position:absolute}

/* top bar */
.topbar{left:0;top:0;width:892px;height:26px;background:var(--brown)}
.pill{position:absolute;height:18px;border-radius:9px;background:var(--orange);color:var(--white);font-size:7.5px;line-height:18px;padding-left:15px;white-space:nowrap}
.pill::before{content:"";position:absolute;left:7px;top:7px;width:4px;height:4px;background:var(--white)}
.logo-cut{left:180px;top:0;width:80px;height:38px;background:var(--white);border-bottom-right-radius:60px}

/* brand */
.brand{left:160px;top:49px;display:flex;align-items:center;gap:6px;white-space:nowrap}
.brand-mark{width:13px;height:13px;background:var(--orange)}
.brand-name{font-family:"Jost",sans-serif;font-weight:500;font-size:11.5px;color:var(--brown);letter-spacing:.2px}

/* nav */
.nav{left:320px;top:47px;display:flex;align-items:center;white-space:nowrap}
.nav a{font-family:"Jost",sans-serif;font-variant:small-caps;font-size:13.5px;color:var(--ink);text-decoration:none;padding:0 8px;height:19px;line-height:18px;display:block}
.nav a.active{background:var(--brown);color:var(--white);border-radius:10px;padding:0 12px}

/* hero */
.hero{left:160px;top:86px;width:572px;height:260px;background:linear-gradient(100deg,#d8dde2 0%,#c7ccd1 30%,#b9bec4 55%,#aeb5bc 75%,#8f969d 100%)}
.hero-panel{left:246px;top:86px;width:100px;height:260px;background:var(--brown-panel);color:var(--white);padding:58px 0 0 14px}
.hero-panel h2{font-family:"Jost",sans-serif;font-weight:400;font-size:13.5px;line-height:16.5px;letter-spacing:.2px}
.hero-panel p{font-size:7.3px;line-height:9.4px;margin-top:5px;width:82px}
.hero-btn{position:absolute;left:12px;top:215px;width:65px;height:14px;border-radius:7px;background:var(--orange);font-family:"Jost",sans-serif;font-variant:small-caps;font-size:8px;line-height:14px;text-align:center}
.hero-arrow{width:18px;height:18px;border-radius:50%;background:rgba(255,255,255,.35)}

/* private access */
.access{left:546px;top:312px;width:172px;height:140px;background:var(--white);box-shadow:0 3px 8px rgba(0,0,0,.18);padding:14px 17px 0}
.access h3{font-family:"Jost",sans-serif;font-weight:500;font-size:15.5px;color:var(--ink);margin-left:2px;white-space:nowrap}
.field{width:136px;height:19px;border:1px solid #d7d7d7;font-size:7.5px;color:#888;line-height:17px;padding-left:7px;margin-top:6px}
.field:first-of-type{margin-top:9px}
.login{width:137px;height:27px;background:var(--brown);color:var(--white);font-family:"Jost",sans-serif;font-weight:600;font-size:11px;text-align:center;line-height:27px;margin-top:6px;letter-spacing:.3px;white-space:nowrap}

/* welcome */
.welcome{left:160px;top:374px;width:370px}
.welcome h1{font-family:"Jost",sans-serif;font-weight:400;font-size:17.5px;color:var(--brown);white-space:nowrap}
.welcome p{font-size:8.4px;line-height:11.2px;color:var(--ink);margin-top:7px}

/* service cards */
.card{top:482px;width:183px;height:184px;background:var(--orange);box-shadow:0 0 0 1px #e2e2e2}
.card h4{position:absolute;left:12px;top:15px;font-family:"Jost",sans-serif;font-weight:500;font-size:11.5px;color:var(--white);display:flex;align-items:center;gap:3px;width:163px;white-space:nowrap}
.card h4::after{content:"";flex:1;height:2px;background:var(--white);margin-top:3px}
.card-img{position:absolute;left:9px;top:40px;width:165px;height:77px}
.card p{position:absolute;left:10px;top:124px;width:165px;font-size:7.6px;line-height:9.6px;color:var(--white)}
.card svg{position:absolute;left:0;bottom:0}
.card .more{position:absolute;left:11px;bottom:3px;font-size:7.5px;font-weight:600;color:var(--ink)}

/* ticker */
.ticker{left:0;top:701px;width:892px;height:23px;background:var(--band);display:flex;padding-left:162px;align-items:center}
.tick{width:83px;font-size:5.6px;color:#2a2a4a;font-weight:600;white-space:nowrap}
.up{color:var(--green)}.down{color:var(--red)}

/* verified */
.verified{left:160px;top:740px;font-family:"Jost",sans-serif;font-weight:400;font-size:19px;color:var(--ink);white-space:nowrap}
.badge{background:#e8e8ec}

/* footer */
.footer{left:0;top:780px;width:892px;height:300px;background:var(--footer)}
.dots{left:0;top:776px;width:892px;height:6px;background:radial-gradient(circle at 3px 3px,var(--footer) 1.6px,transparent 1.8px) 0 0/4px 6px repeat-x}
.col{top:820px}
.col h5{font-family:"Jost",sans-serif;font-weight:600;font-size:11.5px;color:var(--orange);display:flex;align-items:center;gap:4px;white-space:nowrap}
.col ul{list-style:none;margin-top:6px}
.col li{font-size:7.6px;color:#e8e8e8;height:22.4px;line-height:14px;position:relative;padding:2px 0 0 8px;border-bottom:1px dashed #8a8a8a;white-space:nowrap}
.col li:last-child{border-bottom:none}
.col li::before{content:"";position:absolute;left:0;top:7px;width:3.5px;height:3.5px;background:#e8e8e8}
.divider{top:802px;width:1px;height:260px;background:var(--footer-line)}
.fbtn{height:17px;border-radius:9px;background:var(--orange);color:var(--white);font-size:7.5px;line-height:17px;padding-left:15px;position:absolute;white-space:nowrap}
.fbtn::before{content:"";position:absolute;left:7px;top:6.5px;width:4px;height:4px;background:var(--white)}
.social{width:10px;height:10px;border-radius:50%;background:#e8e8e8}

/* legal */
.copy-tab{left:310px;top:1064px;width:266px;height:17px}
.copyright{left:0;top:1073px;width:892px;text-align:center;font-size:8px;color:#555}
.fine{left:160px;width:572px;text-align:center;font-size:5.8px;line-height:7.9px;color:#555}
</style>
</head>
<body>

<header>
  <div class="abs topbar"></div>
  <div class="abs logo-cut"></div>
  <span class="pill" style="left:584px;top:4px;width:72px">Apply Now</span>
  <span class="pill" style="left:659px;top:4px;width:72px">Contact Us</span>

  <div class="abs brand">
    <span class="brand-mark"></span>
    <span class="brand-name">Marlowe Capital Group</span>
  </div>

  <nav class="abs nav">
    <a href="#">Home</a>
    <a href="#" class="active">About</a>
    <a href="#">Investment</a>
    <a href="#">Funds</a>
    <a href="#">Brokerage</a>
    <a href="#">Exchange</a>
    <a href="#">Accounts</a>
  </nav>
</header>

<section>
  <div class="abs hero" role="img" aria-label="Photo of a smiling team of private bankers in business suits in a bright office"></div>
  <div class="abs hero-arrow" style="left:176px;top:203px"></div>
  <div class="abs hero-arrow" style="left:696px;top:203px"></div>
  <div class="abs hero-panel">
    <h2>TEAMWORK<br>FOR YOUR<br>BENEFIT</h2>
    <p>Our dedicated Private Bankers, will proactively keep you up to date with relevant information and provide a financial ovrview that enables you to make lorem ipsum dummy text...</p>
    <span class="hero-btn">Learn More</span>
  </div>

  <div class="abs access">
    <h3>PRIVATE ACCESS</h3>
    <div class="field">Acc. Number</div>
    <div class="field">Acc. Password</div>
    <div class="login">LOGIN TO ACCOUNT</div>
  </div>

  <div class="abs welcome">
    <h1>Welcome to Marlowe Capital Group</h1>
    <p>Lorem ipsum dolor sit amet, consectetur adipisicing elit, sed do eiusmod tempor incididunt ut labore et dolore magna aliqua. Ut enim ad minim veniam, nostrud exercitation ullamco laboris nisi ut aliquip commodo consequatfugiat nulla pariatur. Excepteu Lorem ipsum dolor sit amet, consectetur adipisicing elit, sed do eiusmod tempor incididunt ut labore</p>
  </div>
</section>

<section>
  <article class="abs card" style="left:160px">
    <h4>Management &amp; Strategy</h4>
    <div class="card-img" role="img" aria-label="Photo of a businesswoman presenting a bar chart" style="background:linear-gradient(90deg,#e9e6e2,#d9dde2)"></div>
    <p>Lorem ipsum dolor sit Lorem ipsum dolor sit amet onsectetur amet dolor sit &nbsp;Lorem ipsum dolor sit amet onsectetur</p>
    <svg width="183" height="22" viewBox="0 0 183 22"><path d="M1 0H62C72 0 74 21 90 21H1Z" fill="#fff"/></svg>
    <span class="more">learn more</span>
  </article>
  <article class="abs card" style="left:354px">
    <h4>Funds</h4>
    <div class="card-img" role="img" aria-label="Photo of hands holding a young green plant" style="background:linear-gradient(180deg,#f2f2f0,#e4ddd3 60%,#d9c6b0)"></div>
    <p>Lorem ipsum dolor sit Lorem ipsum dolor sit amet onsectetur amet dolor sit &nbsp;Lorem ipsum dolor sit amet onsectetur</p>
    <svg width="183" height="22" viewBox="0 0 183 22"><path d="M1 0H62C72 0 74 21 90 21H1Z" fill="#fff"/></svg>
    <span class="more">learn more</span>
  </article>
  <article class="abs card" style="left:550px">
    <h4>Currency Exchange</h4>
    <div class="card-img" role="img" aria-label="Photo of a stock exchange board with coloured figures" style="background:linear-gradient(90deg,#3a1414,#1c2a4a 45%,#1f2f1a)"></div>
    <p>Lorem ipsum dolor sit Lorem ipsum dolor sit amet onsectetur amet dolor sit &nbsp;Lorem ipsum dolor sit amet onsectetur</p>
    <svg width="183" height="22" viewBox="0 0 183 22"><path d="M1 0H62C72 0 74 21 90 21H1Z" fill="#fff"/></svg>
    <span class="more">learn more</span>
  </article>
</section>

<div class="abs ticker">
  <span class="tick">GBP / UAH = <span class="up">12.65761 ▲</span></span>
  <span class="tick">GBP / UAH = <span class="down">12.65761 ▼</span></span>
  <span class="tick">GBP / UAH = <span class="up">12.65761 ▲</span></span>
  <span class="tick">GBP / UAH = <span class="up">12.65761 ▲</span></span>
  <span class="tick">GBP / UAH = <span class="down">12.65761 ▼</span></span>
  <span class="tick">GBP / UAH = <span class="up">12.65761 ▲</span></span>
  <span class="tick">GBP / UAH = <span class="up">12.65761 ▲</span></span>
</div>

<div class="abs verified">Verified and Protected by</div>
<div class="abs badge" role="img" aria-label="Security certificate badge" style="left:460px;top:741px;width:52px;height:24px;border-radius:12px"></div>
<div class="abs badge" role="img" aria-label="Privacy certificate badge" style="left:539px;top:743px;width:50px;height:20px"></div>
<div class="abs badge" role="img" aria-label="Audit partner badge" style="left:621px;top:743px;width:43px;height:20px"></div>
<div class="abs badge" role="img" aria-label="Trust seal badge" style="left:707px;top:740px;width:26px;height:26px;border-radius:50%"></div>

<footer>
  <div class="abs footer"></div>
  <div class="abs dots"></div>

  <div class="abs divider" style="left:234px"></div>
  <div class="abs divider" style="left:402px"></div>
  <div class="abs divider" style="left:498px"></div>
  <div class="abs divider" style="left:644px"></div>

  <div class="abs col" style="left:160px;width:62px">
    <h5><svg width="10" height="10" viewBox="0 0 10 10"><path d="M1 5l3 3 5-7" stroke="#f47b20" stroke-width="2.2" fill="none"/></svg>About Us</h5>
    <ul><li>History</li><li>Expertize</li><li>Identity</li><li>Strategy</li><li>Contact us</li></ul>
  </div>
  <div class="abs col" style="left:248px;width:133px">
    <h5><svg width="10" height="10" viewBox="0 0 10 10"><path d="M1 5l3 3 5-7" stroke="#f47b20" stroke-width="2.2" fill="none"/></svg>Investments</h5>
    <ul><li>Term Deposits</li><li>Management &amp; Strategy</li><li>Client Relations</li><li>Financial Privacy</li><li>Tax Advice</li><li>Wealth Analysis &amp; Financial Planning</li><li>Active Adisory Group</li><li>Manager Selection Servoces</li><li>Provate Equity</li></ul>
  </div>
  <div class="abs col" style="left:420px;width:65px">
    <h5><svg width="10" height="10" viewBox="0 0 10 10"><path d="M1 5l3 3 5-7" stroke="#f47b20" stroke-width="2.2" fill="none"/></svg>Funds</h5>
    <ul><li>History</li><li>Expertize</li><li>Identity</li><li>Strategy</li><li>Contact us</li></ul>
  </div>
  <div class="abs col" style="left:514px;width:66px">
    <h5><svg width="10" height="10" viewBox="0 0 10 10"><path d="M1 5l3 3 5-7" stroke="#f47b20" stroke-width="2.2" fill="none"/></svg>Currency Exchange</h5>
    <ul><li>Forign Exchange</li><li>Fx Forward</li><li>Fx Options</li></ul>
  </div>
  <div class="abs col" style="left:514px;top:917px">
    <h5><svg width="10" height="10" viewBox="0 0 10 10"><path d="M1 5l3 3 5-7" stroke="#f47b20" stroke-width="2.2" fill="none"/></svg>Accounts</h5>
  </div>
  <span class="fbtn" style="left:512px;top:944px;width:73px">Apply Now</span>
  <span class="fbtn" style="left:511px;top:966px;width:86px">Private Access</span>

  <div class="abs col" style="left:658px;width:65px">
    <h5><svg width="10" height="10" viewBox="0 0 10 10"><path d="M1 5l3 3 5-7" stroke="#f47b20" stroke-width="2.2" fill="none"/></svg>Brokerage</h5>
    <ul><li>Institutional</li><li>Research</li><li>Traiding</li></ul>
  </div>
  <div class="abs social" role="img" aria-label="Professional network" style="left:663px;top:927px"></div>
  <div class="abs social" role="img" aria-label="Microblog" style="left:681px;top:927px"></div>
  <div class="abs social" role="img" aria-label="Social network" style="left:699px;top:927px"></div>

  <svg class="abs copy-tab" width="266" height="17" viewBox="0 0 266 17"><path d="M14 0H252L266 17H0Z" fill="#fff"/></svg>
  <div class="abs copyright">© 2013 all right reserved with KV Group - Terms - Disclaimer</div>

  <p class="abs fine" style="top:1108px">Lorem ipsum dolor sit amet, consectetur adipiscing elit. In fermentum dolor non augue pretium egestas. Donec sem eros, tincidunt at congue ut, posuere sit amet est. Vivamus scelerisque viverra odio sit amet laoreet. Ut nec neque non justo rutrum tempor lobortis eu ante. Aliquam sagittis, nibh quis commodo auctor, risus mauris laoreet lectus, id facilisis libero odio nec enim. Sed id ligula adipiscing purus lacinia aliquet. Sed eu est non nisl vehicula bibendum congue sit amet enim.</p>
  <p class="abs fine" style="top:1140px">Lorem ipsum dolor sit amet, consectetur adipiscing elit. In fermentum dolor non augue pretium egestas. Donec sem eros, tincidunt at congue ut, posuere sit amet est vivamus scelerisque viverra odio sit amet laoreet. Ut nec neque non justo rutrum tempor lobortis eu ante. Aliquam sagittis, nibh quis commodo auctor, risus mauris laoreet lectus, id facilisis libero odio nec enim. Sed id ligula adipiscing purus lacinia aliquet..</p>
</footer>

</body>
</html>
```